harbor lantern security & electric needs a business card

Must be attractive and modern, look professional and upscale!!
We provide alarm and cameras services and 24 hour monitoring for commercial and residential clients. In addition, the owner is a master electrician that provides services to commercial and residential clients.
We also install and service automatic gates. We previously had two different businesses but decided to merge into one, thus creating Harbor Lantern Security & Electric.

Target Market(s)

Commercial Business and residential customers

Industry/Entity Type

Security

Contact Information for Business Card

Front and back design with logo and services listed

Font styles to use
Sans Serif

Colors
ec1f27
0355a3
fbee3f

Requirements
Must have
• Front of card:
• Marcus Tremblow-Owner
• telephone icon and then the number 936-555-0193
• Mail icon and then email address mtremblow@quillmail.example
• World Icon then website www.yourharborlanterntx.example
• Location marker and then Marlowe Springs, Texas
• We would like to have a picture of the logo at least on the front
• Also need motto on front: Always On When You're Away
• The front of the card must also say Licensed and Insured in addition to:
• License Number: K47315
• TECL: 58629
• On the Back of the Card:
• List each of these Services with check marks:
• Residential and Commercial Electrical Services
• Electric Gates
• Alarm Systems
• Alarm Monitoring
• Cameras
• ***Use separate attached logo, the business card design is just to be used as a model***
Nice to have
• It would be nice to have the logo on back of the card in addition to these words at the bottom:
• "No job too big or small, we do it all!"
Should not have
• Anything crazy!!

```html
<!DOCTYPE html>
<html lang="en">
<head>
<meta charset="utf-8">
<title>Harbor Lantern Security &amp; Electric — Business Card</title>
<link rel="stylesheet" href="https://fonts.googleapis.com/css2?family=Michroma&family=Exo+2:wght@500;600;700&family=Tinos&display=swap">
<style>
  :root {
    --red: #ec1f27;
    --red-soft: #f0553a;
    --navy: #2c4a86;
    --ink: #161616;
    --paper: #ffffff;
    --stage: #e4e4e6;
  }
  * { box-sizing: border-box; margin: 0; padding: 0; }
  html, body { width: 1200px; height: 900px; overflow: hidden; }
  body {
    background: var(--stage);
    font-family: "Exo 2", sans-serif;
    position: relative;
  }
  .card {
    position: absolute;
    width: 700px;
    height: 400px;
    left: 250px;
    overflow: hidden;
    box-shadow: 0 10px 30px rgba(0,0,0,.18);
  }

  /* ---------- Back ---------- */
  .card-back { top: 30px; background: var(--red); }
  .back-frame {
    position: absolute;
    left: 46px; top: 30px; right: 30px; bottom: 34px;
    border: 1.5px solid var(--paper);
  }
  .frame-dot {
    position: absolute; left: -5px;
    width: 9px; height: 9px; border-radius: 50%;
    background: var(--paper);
  }
  .frame-dot.top { top: 46px; }
  .frame-dot.bottom { top: 130px; }
  .back-emblem {
    position: absolute;
    right: 10px; top: 70px;
    width: 330px; height: 330px;
    border-radius: 40% 30% 20% 45%;
    background: radial-gradient(circle at 45% 40%, rgba(255,120,80,.55), rgba(255,110,70,.18) 60%, rgba(236,31,39,0) 75%);
  }
  .service-list {
    position: absolute;
    left: 76px; top: 66px;
    list-style: none;
    font-family: "Tinos", serif;
    color: var(--paper);
    font-size: 17px;
    line-height: 21px;
  }
  .service-list li { display: flex; align-items: center; gap: 10px; }
  .service-list li::before {
    content: ""; width: 10px; height: 10px; background: var(--paper); flex: none;
  }

  /* ---------- Front ---------- */
  .card-front { top: 470px; background: var(--paper); }
  .front-emblem {
    position: absolute;
    left: 390px; top: 60px;
    width: 300px; height: 250px;
    border-radius: 30% 20% 45% 40%;
    background: radial-gradient(circle at 55% 50%, rgba(44,74,134,.10), rgba(236,31,39,.07) 55%, rgba(255,255,255,0) 75%);
  }
  .owner { position: absolute; left: 46px; top: 40px; }
  .owner-name {
    font-family: "Michroma", sans-serif;
    font-size: 19px; color: var(--ink); letter-spacing: .5px;
  }
  .owner-title {
    font-family: "Michroma", sans-serif;
    font-size: 11px; color: var(--red); margin-top: 2px;
  }
  .contact-list {
    position: absolute; left: 46px; top: 118px;
    list-style: none; font-size: 15px; font-weight: 600; color: var(--ink);
  }
  .contact-list li { display: flex; align-items: center; gap: 8px; height: 22px; }
  .contact-list svg { width: 15px; height: 15px; flex: none; }
  .license {
    position: absolute; left: 46px; top: 216px;
    font-size: 15px; font-weight: 600; color: var(--ink); line-height: 21px;
  }
  .license .num { color: var(--red); }
  .rule {
    position: absolute; height: 1.5px; background: var(--red);
  }
  .rule-main { left: 0; top: 286px; width: 460px; }
  .rule-side { left: 630px; top: 334px; width: 70px; }
  .rule-dot {
    position: absolute; width: 9px; height: 9px; border-radius: 50%; background: var(--red);
  }
  .motto {
    position: absolute; left: 40px; top: 298px;
    font-family: "Michroma", sans-serif;
    font-size: 15px; color: var(--red); letter-spacing: .3px;
  }
  .band { position: absolute; left: 0; right: 0; bottom: 0; height: 34px; display: flex; }
  .band-red { width: 44%; background: var(--red); }
  .band-navy { flex: 1; background: var(--navy); }

  .brand {
    position: absolute; left: 400px; top: 140px; width: 290px;
    display: flex; align-items: center; gap: 12px;
  }
  .brand-dot { width: 22px; height: 22px; border-radius: 50%; background: var(--red); flex: none; }
  .brand-name {
    font-family: "Michroma", sans-serif;
    font-size: 20px; line-height: 26px; color: var(--navy);
  }

  .badge {
    position: absolute; left: 470px; top: 300px;
    width: 150px; height: 64px;
    border: 3px solid var(--red); border-radius: 10px; padding: 3px;
    background: var(--paper);
  }
  .badge-inner {
    width: 100%; height: 100%; border-radius: 7px; background: var(--red);
    display: flex; align-items: center; gap: 8px; padding: 0 10px;
  }
  .badge-inner svg { width: 26px; height: 26px; flex: none; }
  .badge-text {
    font-family: "Michroma", sans-serif; color: var(--paper);
    font-size: 12px; line-height: 13px; text-align: center;
  }
  .badge-text small { display: block; font-family: "Exo 2", sans-serif; font-size: 9px; line-height: 9px; }
</style>
</head>
<body>

  <section class="card card-back" aria-label="Business card, back">
    <div class="back-emblem" role="img" aria-label="Faint security camera illustration"></div>
    <div class="back-frame">
      <span class="frame-dot top"></span>
      <span class="frame-dot bottom"></span>
    </div>
    <ul class="service-list">
      <li>Residential and Commercial Electrical Services</li>
      <li>Electric Gates</li>
      <li>Alarm Systems</li>
      <li>Alarm Monitoring</li>
      <li>Cameras</li>
    </ul>
  </section>

  <section class="card card-front" aria-label="Business card, front">
    <div class="front-emblem" role="img" aria-label="Faint oversized security emblem decoration"></div>

    <div class="owner">
      <div class="owner-name">MARCUS TREMBLOW</div>
      <div class="owner-title">OWNER</div>
    </div>

    <ul class="contact-list">
      <li>
        <svg viewBox="0 0 16 16"><rect width="16" height="16" rx="3" fill="#ec1f27"/><path d="M5 3.5l2 2-1 1.2c.6 1.3 1.6 2.3 2.9 2.9l1.2-1 2 2-1.2 1.6C7.5 12 4 8.5 3.8 4.7z" fill="#fff"/></svg>
        936-555-0193
      </li>
      <li>
        <svg viewBox="0 0 16 16"><rect width="16" height="16" rx="3" fill="#ec1f27"/><rect x="3" y="4.5" width="10" height="7" fill="none" stroke="#fff" stroke-width="1.3"/><path d="M3 4.5l5 4 5-4" fill="none" stroke="#fff" stroke-width="1.3"/></svg>
        mtremblow@quillmail.example
      </li>
      <li>
        <svg viewBox="0 0 16 16"><rect width="16" height="16" rx="3" fill="#ec1f27"/><circle cx="8" cy="8" r="5" fill="none" stroke="#fff" stroke-width="1.2"/><ellipse cx="8" cy="8" rx="2.2" ry="5" fill="none" stroke="#fff" stroke-width="1"/><path d="M3 8h10" stroke="#fff" stroke-width="1"/></svg>
        www.yourharborlanterntx.example
      </li>
      <li>
        <svg viewBox="0 0 16 16"><rect width="16" height="16" rx="3" fill="#ec1f27"/><path d="M8 13.5S4 9.4 4 6.6a4 4 0 018 0c0 2.8-4 6.9-4 6.9z" fill="#fff"/><circle cx="8" cy="6.5" r="1.5" fill="#ec1f27"/></svg>
        Marlowe Springs, Texas
      </li>
    </ul>

    <div class="license">
      <div>License Number: <span class="num">K47315</span></div>
      <div>TECL: <span class="num">58629</span></div>
    </div>

    <div class="brand">
      <span class="brand-dot"></span>
      <div class="brand-name">Harbor Lantern Security &amp; Electric</div>
    </div>

    <div class="rule rule-main"></div>
    <span class="rule-dot" style="left:456px;top:282px"></span>
    <div class="rule rule-side"></div>
    <span class="rule-dot" style="left:626px;top:330px"></span>

    <div class="motto">ALWAYS ON WHEN YOU'RE AWAY</div>

    <div class="badge">
      <div class="badge-inner">
        <svg viewBox="0 0 26 26"><circle cx="13" cy="13" r="11" fill="none" stroke="#fff" stroke-width="2"/><path d="M7.5 13.5l4 4 7-8" fill="none" stroke="#fff" stroke-width="2.4" stroke-linecap="round" stroke-linejoin="round"/></svg>
        <div class="badge-text">LICENSED<small>and</small>INSURED</div>
      </div>
    </div>

    <div class="band">
      <div class="band-red"></div>
      <div class="band-navy"></div>
    </div>
  </section>

</body>
</html>
```